Design a modern, classy & professional business card for an online real estate agency, specializing in medium-luxury properties in Thailand and later in Singapore and UK.

Possible design ideas so far: (not essential)

- curved corner(s) to the card, white on front & turquoise on back or visa versa.

- front of card - clear and simple, company name in metallic grey/monochrome, logo graphic & company name on front in spot UV or embossed/debossed effect.

- back of card - large, close-cropped, 'ghost' patterns of the C-shaped curves of logo, or company name repeated on back of card in spot UV.

Target Market(s)

- young to middle-aged professionals mainly (but ideally should design should suit all)

- UK, US,EU,AUS & ASIAN mainly (but ideally should design should suit all countries)

Industry/Entity Type

Real Estate

Requirements
Must have
• THEME:
- Luxurious & Modern
- Clean & striking
- Unique & creative

INFO:
- Logo & company name on front
- Contact details on back:

Tobias Lindqvist
Managing Director

www.velmoraestates.example
www.velmoraestates-uk.example

Tel: 083-274-6190
email: tobias@velmoraestates.example

(contact details can be displayed in any order as suites design.)

Nice to have
• - curved corner(s) to the card, white on front & turquoise on back or visa versa.

Should not have
• - No generic images of properties, palm trees/coconut trees etc.

- No other other bold colors, except for main turquoise, grey, metallic white & black theme.

- No obvious business card templates

```html
<!DOCTYPE html>
<html lang="en">
<head>
<meta charset="utf-8">
<title>Velmora Estates – Business Card</title>
<link rel="stylesheet" href="https://fonts.googleapis.com/css2?family=Saira:wght@400;500;600&display=swap">
<style>
  :root {
    --turquoise: #14c7c6;
    --ink: #1c2a31;
    --grey: #77797b;
    --arc-grey: #8a8b8d;
    --paper: #f7f7f7;
    --backdrop: #e6e4e0;
  }
  * { box-sizing: border-box; margin: 0; padding: 0; }
  html, body {
    width: 1200px; height: 900px; overflow: hidden;
    background: var(--backdrop);
    font-family: "Saira", sans-serif;
  }
  .business-card {
    position: absolute; left: 100px; top: 165px;
    width: 1000px; height: 570px;
    background: var(--paper);
    box-shadow: 0 10px 30px rgba(0,0,0,.12);
    overflow: hidden;
  }
  .card-shapes { position: absolute; inset: 0; }
  .contact-panel {
    position: absolute; left: 62px; top: 52px;
    color: var(--ink);
  }
  .holder-name {
    font-size: 31px; font-weight: 600; letter-spacing: 1.5px;
    text-transform: uppercase; line-height: 1.1;
  }
  .holder-title { font-size: 21px; font-weight: 400; margin-top: 4px; }
  .office-address {
    font-size: 21px; font-weight: 400; line-height: 1.35;
    margin-top: 34px; font-style: normal;
  }
  .contact-list { list-style: none; margin-top: 40px; }
  .contact-item {
    display: flex; align-items: center; gap: 14px;
    font-size: 19px; line-height: 1; height: 38px;
  }
  .contact-item svg { width: 20px; height: 20px; fill: var(--ink); flex: none; }
  .brand-block {
    position: absolute; left: 640px; top: 170px; width: 300px;
    display: flex; flex-direction: column; align-items: center;
  }
  .brand-square { width: 112px; height: 112px; background: var(--turquoise); }
  .brand-name {
    margin-top: 18px; color: var(--grey);
    font-weight: 500; text-align: center; line-height: 1;
  }
  .brand-name .word-main { display: block; font-size: 62px; }
  .brand-name .word-sub { display: block; font-size: 25px; letter-spacing: 9px; margin-top: 8px; padding-left: 9px; }
</style>
</head>
<body>
  <main class="business-card">
    <svg class="card-shapes" viewBox="0 0 1000 570" width="1000" height="570" aria-hidden="true">
      <path class="turquoise-panel" fill="var(--turquoise)" d="M0 0 H600 C470 90 400 300 450 570 H0 Z"/>
      <path class="grey-arc" fill="var(--arc-grey)" d="M640 0 C505 100 440 300 478 570 L468 570 C425 300 490 90 622 0 Z"/>
    </svg>

    <section class="contact-panel">
      <h1 class="holder-name">Tobias Lindqvist</h1>
      <p class="holder-title">Managing Director</p>
      <address class="office-address">21 Harbour Row, 9th floor<br>Linden Road LKP</address>
      <ul class="contact-list">
        <li class="contact-item">
          <svg viewBox="0 0 24 24"><path d="M6.6 10.8a15 15 0 0 0 6.6 6.6l2.2-2.2c.3-.3.7-.4 1-.2 1.1.4 2.3.6 3.6.6.6 0 1 .4 1 1V20c0 .6-.4 1-1 1A17 17 0 0 1 3 4c0-.6.4-1 1-1h3.5c.6 0 1 .4 1 1 0 1.3.2 2.5.6 3.6.1.3 0 .7-.2 1z"/></svg>
          <span>083-274-6190</span>
        </li>
        <li class="contact-item">
          <svg viewBox="0 0 24 24"><path d="M7 1h10a2 2 0 0 1 2 2v18a2 2 0 0 1-2 2H7a2 2 0 0 1-2-2V3a2 2 0 0 1 2-2zm0 3v14h10V4zm5 15.5a1.2 1.2 0 1 0 0 2.4 1.2 1.2 0 0 0 0-2.4z"/></svg>
          <span>083-274-6190</span>
        </li>
        <li class="contact-item">
          <svg viewBox="0 0 24 24"><path d="M6 2h9l3 3v5h1a3 3 0 0 1 3 3v9H2v-9a3 3 0 0 1 3-3h1zm2 2v6h8V6h-2V4zm-2 11v2h2v-2zm4 0v2h2v-2zm4 0v2h2v-2z"/></svg>
          <span>083-274-6190</span>
        </li>
        <li class="contact-item">
          <svg viewBox="0 0 24 24"><path d="M2 5h20v14H2zm2 2v.5l8 5 8-5V7zm0 2.8V17h16V9.8l-8 5z"/></svg>
          <span>tobias@velmoraestates.example</span>
        </li>
        <li class="contact-item">
          <svg viewBox="0 0 24 24"><path d="M12 2a10 10 0 1 0 0 20 10 10 0 0 0 0-20zm6.9 6h-3a15 15 0 0 0-1.3-3.9A8 8 0 0 1 18.9 8zM12 4c.9 1.2 1.5 2.6 1.9 4h-3.8c.4-1.4 1-2.8 1.9-4zM4.3 14a8 8 0 0 1 0-4h3.4a16 16 0 0 0 0 4zm.8 2h3a15 15 0 0 0 1.3 3.9A8 8 0 0 1 5.1 16zm3-8h-3a8 8 0 0 1 4.3-3.9C8.8 5.3 8.4 6.6 8.1 8zM12 20c-.9-1.2-1.5-2.6-1.9-4h3.8c-.4 1.4-1 2.8-1.9 4zm2.3-6H9.7a14 14 0 0 1 0-4h4.6a14 14 0 0 1 0 4zm.3 5.9c.6-1.2 1-2.5 1.3-3.9h3a8 8 0 0 1-4.3 3.9zm1.7-5.9a16 16 0 0 0 0-4h3.4a8 8 0 0 1 0 4z"/></svg>
          <span>www.velmoraestates.example</span>
        </li>
      </ul>
    </section>

    <section class="brand-block">
      <div class="brand-square" aria-hidden="true"></div>
      <p class="brand-name"><span class="word-main">Velmora</span><span class="word-sub">ESTATES</span></p>
    </section>
  </main>
</body>
</html>
```